Quillory Points website re-design and

the institute of massage therapy is ready for a new website. The current website is around 12 years old and it looks old. Luckily the clients is not against changing the colors so the new design does not have to use the current ugly green color scheme. Be creative! Make it pretty, modern and inviting. The current colors look like mold. Nobody likes mold. I have attached the logo asset file as well as a txt document that details the new website design parameters

1 page

```html
<!DOCTYPE html>
<html lang="en">
<head>
<meta charset="utf-8">
<title>Quillory Points</title>
<link rel="stylesheet" href="https://fonts.googleapis.com/css2?family=Almendra+SC&family=Roboto:wght@400;500&display=swap">
<style>
:root{
  --rose:#dbaea5;
  --rose-dark:#c9968c;
  --slate:#4b5b70;
  --footer:#5d6c82;
  --text:#707070;
  --white:#ffffff;
  --mist:#ece8e8;
}
*{box-sizing:border-box;margin:0;padding:0}
html,body{width:1200px;height:3914px;overflow:hidden}
body{font-family:"Roboto",Arial,sans-serif;color:var(--text);background:var(--white);position:relative}
.display{font-family:"Almendra SC",Georgia,serif;font-weight:400;text-transform:uppercase;letter-spacing:1.5px;-webkit-text-stroke:0.6px currentColor}
.btn{display:inline-flex;align-items:center;justify-content:center;background:var(--rose);color:var(--white);font-size:15px;font-weight:500;text-transform:uppercase;border-radius:4px;height:50px;box-shadow:0 3px 6px rgba(0,0,0,.12)}

/* header */
.site-header{position:absolute;top:0;left:0;width:1200px;height:96px;background:var(--white)}
.brand{position:absolute;left:64px;top:30px;display:flex;align-items:center;gap:12px;font-size:22px;font-weight:500;color:#222}
.brand-dot{width:34px;height:34px;border-radius:50%;background:#222}
.main-nav{position:absolute;left:378px;top:40px;display:flex;gap:20px;font-size:14px;color:var(--slate);text-transform:uppercase}
.main-nav .active{color:var(--rose);border-bottom:2px solid var(--rose);padding-bottom:8px}
.login-btn{position:absolute;left:906px;top:23px;width:117px;height:50px;border:2px solid var(--rose);border-radius:4px;display:flex;align-items:center;justify-content:center;gap:9px;color:var(--slate);font-size:15px;font-weight:500}
.cart-btn{position:absolute;left:1031px;top:23px;width:52px;height:50px;background:var(--rose);border-radius:4px;display:flex;align-items:center;justify-content:center}
.cart-info{position:absolute;left:1097px;top:26px;font-size:13px;color:var(--slate);line-height:24px}
.cart-info span{color:var(--rose)}

/* hero */
.hero{position:absolute;top:96px;left:0;width:1200px;height:600px;background:linear-gradient(110deg,#e7e1dc 0%,#d9cfc8 40%,#c8a58e 70%,#b9937c 100%)}
.hero h1{position:absolute;left:111px;top:185px;width:640px;color:var(--white);font-size:37px;line-height:45px}
.hero-search{position:absolute;left:111px;top:352px;display:flex;gap:8px}
.field{height:50px;background:var(--white);border-radius:4px;font-size:14px;color:#555;display:flex;align-items:center;padding:0 16px}
.field.search{width:240px}
.field.select{width:243px;justify-content:space-between}
.hero-search .btn{width:119px;height:50px;margin-left:1px}
.slider-dots{position:absolute;left:1136px;top:262px;display:flex;flex-direction:column;gap:9px}
.slider-dots i{width:14px;height:14px;border:2px solid var(--white);border-radius:50%}
.slider-dots i.on{background:var(--white)}
.badge{position:absolute;left:550px;top:621px;width:100px;height:100px;border-radius:50%;background:rgba(255,255,255,.35);display:flex;align-items:center;justify-content:center;z-index:3}
.badge span{width:72px;height:72px;border-radius:50%;background:var(--white);box-shadow:0 3px 10px rgba(0,0,0,.15)}

/* about */
.about{position:absolute;top:696px;left:0;width:1200px;height:664px;background:linear-gradient(180deg,#ebe7e8 0%,#e6e0de 60%,#ddd3cc 100%)}
.about-visual{position:absolute;left:111px;top:80px;width:410px;height:450px;border-radius:50%;background:radial-gradient(circle,#f4ddc2 0%,#e7d2c2 45%,rgba(230,224,222,0) 72%)}
.about h2{position:absolute;left:589px;top:100px;width:420px;font-size:35px;line-height:44px;color:var(--slate)}
.about-copy{position:absolute;left:589px;top:218px;width:500px;font-size:13.5px;line-height:25.6px;text-align:justify}
.about-copy p+p{margin-top:15px}
.about-curve{position:absolute;left:0;top:1180px;width:1200px;height:185px;z-index:2}

/* packages */
.section-title{position:absolute;left:0;width:1200px;text-align:center;font-size:35px;color:var(--slate)}
.packages{position:absolute;top:1514px;left:111px;display:flex;gap:22px}
.pkg{width:311px;height:424px;background:var(--white);border-radius:6px;box-shadow:0 2px 10px rgba(0,0,0,.13);padding:8px;text-align:center}
.pkg .photo{height:200px}
.pkg h3{margin-top:24px;font-size:17.5px;font-weight:500;color:var(--slate);text-transform:uppercase}
.pkg p{margin:11px 8px 0;font-size:12px;line-height:23px;height:69px}
.pkg .btn{margin-top:19px;width:145px}

/* certifications */
.certs{position:absolute;top:2035px;left:0;width:1200px;height:446px;background:var(--rose)}
.certs .section-title{color:var(--white);top:52px}
.cert-row{position:absolute;left:111px;top:137px;display:flex;gap:24px}
.cert{width:226px;height:246px;background:var(--white);border-radius:6px;padding:7px;text-align:center}
.cert .photo{height:141px;background:linear-gradient(135deg,#e4ded2,#cfc6b4);display:flex;align-items:flex-end;justify-content:center;padding-bottom:18px}
.cert .seal{width:26px;height:26px;border-radius:50%;background:#c9a44b}
.cert h4{margin-top:17px;font-size:13px;font-weight:400;line-height:23px;color:var(--slate);text-transform:uppercase}
.cert small{display:block;margin-top:4px;font-size:12.5px}

/* free course */
.free{position:absolute;top:2481px;left:0;width:1200px;height:445px;background:linear-gradient(90deg,#e6d9cf 0%,#efe6df 45%,#f2efef 70%,#f3f2f3 100%)}
.free-card{position:absolute;left:652px;top:82px;width:437px;height:281px;background:rgba(255,255,255,.75);border-radius:20px;text-align:center}
.free-card h2{margin-top:48px;font-size:31px;color:var(--slate)}
.free-card p{margin:18px auto 0;width:320px;font-size:16px;line-height:26px;color:#555}
.free-card .btn{margin-top:22px;width:146px}

/* shop */
.shop{position:absolute;top:3085px;left:111px;display:flex;gap:22px}
.course{width:311px;text-align:center}
.course .photo{height:214px;border-radius:8px}
.course h3{margin-top:36px;font-size:17.5px;font-weight:500;color:var(--slate);text-transform:uppercase}
.course p{margin:10px 10px 0;font-size:12.5px;line-height:23px;height:69px}
.course .btn{margin-top:19px;width:137px}

/* footer */
.site-footer{position:absolute;top:3573px;left:0;width:1200px;height:341px;background:var(--footer);color:var(--white);text-align:center}
.footer-brand{position:absolute;left:0;width:1200px;top:42px;display:flex;justify-content:center;align-items:center;gap:12px;font-size:24px;font-weight:500}
.footer-brand i{width:36px;height:36px;border-radius:50%;background:var(--white)}
.footer-nav{position:absolute;top:122px;left:0;width:1200px;display:flex;justify-content:center;gap:22px;font-size:17px;font-weight:500}
.footer-nav b{font-weight:400}
.footer-contact{position:absolute;top:166px;left:0;width:1200px;display:flex;justify-content:center;align-items:center;gap:22px;font-size:16px}
.footer-contact span{display:flex;align-items:center;gap:12px}
.footer-login{position:absolute;left:542px;top:211px;width:116px}
.footer-rule{position:absolute;left:111px;top:285px;width:978px;height:1px;background:rgba(255,255,255,.3)}
.copyright{position:absolute;top:302px;left:0;width:1200px;font-size:13px}
</style>
</head>
<body>

<header class="site-header">
  <div class="brand"><span class="brand-dot"></span>Quillory Points</div>
  <nav class="main-nav">
    <span class="active">Home</span><span>About</span><span>Courses</span><span>Guidelines</span><span>FAQ</span><span>Policies</span><span>Contact</span>
  </nav>
  <div class="login-btn">
    <svg width="16" height="16" viewBox="0 0 16 16"><circle cx="8" cy="8" r="7" fill="none" stroke="#4b5b70" stroke-width="1.5"/><circle cx="8" cy="6.5" r="2.3" fill="#4b5b70"/><path d="M3.8 12.4c1-1.8 2.4-2.6 4.2-2.6s3.2.8 4.2 2.6" fill="#4b5b70"/></svg>
    LOGIN
  </div>
  <div class="cart-btn">
    <svg width="18" height="18" viewBox="0 0 18 18"><path d="M6 6V4.5a3 3 0 0 1 6 0V6" fill="none" stroke="#fff" stroke-width="1.6"/><rect x="3" y="6" width="12" height="10" rx="1" fill="#fff"/></svg>
  </div>
  <div class="cart-info">Cart:<br><span>$00.00</span></div>
</header>

<section class="hero" role="img" aria-label="Photo of a smiling woman receiving a shoulder massage on a spa table with candles and herbal compresses">
  <h1 class="display">Committed to excellence in massage therapy continuing education</h1>
  <div class="hero-search">
    <div class="field search">Search...</div>
    <div class="field select">Number of CE Hours
      <svg width="10" height="6" viewBox="0 0 10 6"><path d="M1 1l4 4 4-4" fill="none" stroke="#555" stroke-width="1.4"/></svg>
    </div>
    <div class="btn">Search</div>
  </div>
  <div class="slider-dots"><i></i><i class="on"></i><i></i><i></i></div>
</section>

<div class="badge"><span></span></div>

<section class="about">
  <div class="about-visual" role="img" aria-label="Soft photo of lit candles and white orchids"></div>
  <h2 class="display">Quillory Points</h2>
  <div class="about-copy">
    <p>Quillory Points is committed to providing the best online home study continuing education courses available to massage therapists. Quillory Points is approved by the National Board for Touch and Bodywork (NBTB) as a continuing education Approved Provider. Provider # 514208-00. Our massage CEUs/credits are also valid for TMTA and ABWP.</p>
    <p>We are approved by the Gulfshore Massage Licensing Council (Provider #MCE902) and CE Ledgerly (Provider #50-7734). Our massage therapy continuing education courses are valid for most state massage therapy CEU requirements. See our State Guidelines page for specific information about the continuing education laws in your state.</p>
  </div>
</section>
<svg class="about-curve" viewBox="0 0 1200 185" preserveAspectRatio="none">
  <path d="M0 0 Q600 300 1200 0 L1200 185 L0 185 Z" fill="#ffffff"/>
  <path d="M0 0 Q600 300 1200 0" fill="none" stroke="#dbaea5" stroke-width="5"/>
</svg>

<h2 class="section-title display" style="top:1432px">Popular Packages</h2>
<div class="packages">
  <article class="pkg">
    <div class="photo" role="img" aria-label="Photo of a back massage beside herbal compresses and flowers" style="background:linear-gradient(135deg,#e9d8cc,#c7a58f)"></div>
    <h3>Board Certified Renewal</h3>
    <p>Quillory Points is approved by the NBTB (Provider #514208-00) as a continuing education Approved Provider.</p>
    <div class="btn">View Details</div>
  </article>
  <article class="pkg">
    <div class="photo" role="img" aria-label="Photo of a woman relaxing during a massage in a dim candlelit room" style="background:linear-gradient(135deg,#6b4a36,#2c1d15)"></div>
    <h3>Florida Renewal 6 CE</h3>
    <p>Massage Therapy Continuing education CEs available: 7 (1 Diversity, 3 Communicable Diseases/HIV, 3 Ethics Boundary Setting).</p>
    <div class="btn">View Details</div>
  </article>
  <article class="pkg">
    <div class="photo" role="img" aria-label="Photo of a woman receiving a relaxing back massage" style="background:linear-gradient(135deg,#b48a6e,#6d4a37)"></div>
    <h3>Maryland Package</h3>
    <p>Quillory Points is approved by the NBTB (Provider #514208-00) as a continuing education Approved Provider.</p>
    <div class="btn">View Details</div>
  </article>
</div>

<section class="certs">
  <h2 class="section-title display">Our Certifications</h2>
  <div class="cert-row">
    <div class="cert"><div class="photo" role="img" aria-label="Certificate of achievement"><span class="seal"></span></div><h4>Certified Fertility Massage Therapist</h4><small>Credit Hours: 16</small></div>
    <div class="cert"><div class="photo" role="img" aria-label="Certificate of achievement"><span class="seal"></span></div><h4>Certified Infant Massage Therapist–Instructor</h4><small>Credit Hours: 16</small></div>
    <div class="cert"><div class="photo" role="img" aria-label="Certificate of achievement"><span class="seal"></span></div><h4>Certified Massage<br>Doula</h4><small>Credit Hours: 21</small></div>
    <div class="cert"><div class="photo" role="img" aria-label="Certificate of achievement"><span class="seal"></span></div><h4>Certified Prenatal Massage Therapist</h4><small>Credit Hours: 24</small></div>
  </div>
</section>

<section class="free" role="img" aria-label="Photo of a relaxed woman lying down while receiving a back massage">
  <div class="free-card">
    <h2 class="display">Take a free course</h2>
    <p>Click here to get started today &amp; try our FREE online course!</p>
    <div class="btn">Get Started</div>
  </div>
</section>

<h2 class="section-title display" style="top:3004px">Shop Our Courses</h2>
<div class="shop">
  <article class="course">
    <div class="photo" role="img" aria-label="Photo of hands massaging a pregnant belly" style="background:linear-gradient(135deg,#f1e3db,#d6b7a5)"></div>
    <h3>Pregnancy / Doula</h3>
    <p>Courses and packages to become certified in every stage of childbearing, from infertility to infant massage</p>
    <div class="btn">Learn More</div>
  </article>
  <article class="course">
    <div class="photo" role="img" aria-label="Photo of a man receiving a head massage" style="background:linear-gradient(135deg,#e8c9a6,#b98562)"></div>
    <h3>Florida Laws &amp; Packages</h3>
    <p>Courses and packages required to obtain, reinstate, or renew your Florida massage therapy license</p>
    <div class="btn">Learn More</div>
  </article>
  <article class="course">
    <div class="photo" role="img" aria-label="Photo of a therapist giving a deep back massage" style="background:linear-gradient(135deg,#a98a76,#5e4637)"></div>
    <h3>Research Courses</h3>
    <p>Courses approved by the NBTB to earn mandated research hours for Board Certification renewal</p>
    <div class="btn">Learn More</div>
  </article>
</div>

<footer class="site-footer">
  <div class="footer-brand"><i></i>Quillory Points</div>
  <nav class="footer-nav">
    <span>HOME</span><b>|</b><span>ABOUT</span><b>|</b><span>COURSES</span><b>|</b><span>GUIDELINES</span><b>|</b><span>FAQ</span><b>|</b><span>POLICIES</span><b>|</b><span>CONTACT</span>
  </nav>
  <div class="footer-contact">
    <span><svg width="15" height="15" viewBox="0 0 24 24"><path d="M6.6 10.8a15.1 15.1 0 0 0 6.6 6.6l2.2-2.2a1 1 0 0 1 1-.25 11.4 11.4 0 0 0 3.6.57 1 1 0 0 1 1 1V20a1 1 0 0 1-1 1A17 17 0 0 1 3 4a1 1 0 0 1 1-1h3.5a1 1 0 0 1 1 1c0 1.25.2 2.45.57 3.57a1 1 0 0 1-.25 1z" fill="#dbaea5"/></svg>555-014-2290</span>
    <b style="font-weight:400">|</b>
    <span><svg width="16" height="12" viewBox="0 0 16 12"><rect width="16" height="12" rx="1" fill="#dbaea5"/><path d="M0.5 1l7.5 6 7.5-6" fill="none" stroke="#5d6c82" stroke-width="1.3"/></svg>hello@quillorypoints.example</span>
  </div>
  <div class="btn footer-login">
    <svg width="15" height="15" viewBox="0 0 16 16" style="margin-right:8px"><circle cx="8" cy="8" r="7" fill="none" stroke="#fff" stroke-width="1.5"/><circle cx="8" cy="6.5" r="2.3" fill="#fff"/><path d="M3.8 12.4c1-1.8 2.4-2.6 4.2-2.6s3.2.8 4.2 2.6" fill="#fff"/></svg>
    Login
  </div>
  <div class="footer-rule"></div>
  <div class="copyright">© 2022 QUILLORY POINTS &nbsp;/&nbsp; All Rights Reserved</div>
</footer>

</body>
</html>
```